Landing Page IT Security Vendor

We need a landing page that uses our colour scheme (www.veldonguard.com). We created a draft (see attached). We do not need standard stock template design pages. Please only apply if you can design pages from scratch and try to be as close as possible to our draft. It is ok to also purchase commecrial stock pictures

Coding

Coded - Design and coding required

Number of Pages Required

1 page

```html
<!DOCTYPE html>
<html lang="en">
<head>
<meta charset="utf-8">
<title>Veldon – Security Awareness Training</title>
<link href="https://fonts.googleapis.com/css2?family=Poppins:wght@300;400;500;600;700&display=swap" rel="stylesheet">
<style>
  :root {
    --teal: #22c3c6;
    --teal-dark: #14a9b0;
    --teal-soft: #d9f5f5;
    --ink: #23232f;
    --muted: #8a8f99;
    --faint: #eef0f2;
    --white: #ffffff;
    --brand-orange: #f2a23a;
  }
  * { box-sizing: border-box; margin: 0; padding: 0; }
  html, body { width: 796px; height: 1200px; overflow: hidden; }
  body { font-family: "Poppins", sans-serif; color: var(--ink); background: var(--white); position: relative; }

  .site-header { position: absolute; top: 0; left: 0; width: 796px; height: 70px; z-index: 3; }
  .brand { position: absolute; left: 26px; top: 22px; display: flex; align-items: center; gap: 8px; font-size: 22px; font-weight: 700; color: var(--ink); }
  .brand-dot { width: 26px; height: 26px; border-radius: 50%; background: var(--brand-orange); }
  .main-nav { position: absolute; right: 50px; top: 50px; display: flex; gap: 30px; font-size: 10px; font-weight: 500; letter-spacing: .5px; color: var(--ink); }

  .hero-visual { position: absolute; right: 0; top: 0; width: 300px; height: 400px;
    background: radial-gradient(circle at 70% 35%, #2f2a2c 0 22%, transparent 23%),
                linear-gradient(160deg, var(--teal-soft) 0%, #ffffff 45%, var(--teal) 100%);
    border-bottom-left-radius: 140px; z-index: 1; }
  .hero-ghost { position: absolute; left: -20px; top: 236px; font-size: 70px; font-weight: 700; color: var(--faint); white-space: nowrap; z-index: 0; }
  .hero-icon { position: absolute; left: 596px; top: 206px; width: 34px; height: 34px; border-radius: 50%; background: var(--teal); z-index: 2; }
  .hero-mark { position: absolute; left: 596px; top: 206px; z-index: 2; }

  .hero-copy { position: absolute; left: 45px; top: 108px; z-index: 2; }
  .eyebrow { font-size: 10px; font-weight: 500; letter-spacing: 1.5px; color: var(--teal); text-transform: uppercase; }
  .hero-title { margin-top: 10px; font-size: 34px; line-height: 44px; font-weight: 500; color: var(--ink); }
  .demo-row { margin-top: 28px; display: flex; align-items: center; gap: 20px; }
  .btn-outline { display: inline-block; width: 168px; height: 34px; line-height: 32px; text-align: center; border: 1.5px solid var(--teal); border-radius: 17px; font-size: 10px; font-weight: 500; letter-spacing: 1px; color: var(--teal); background: var(--white); box-shadow: 0 6px 14px rgba(34,195,198,.18); }

  .award-band { position: absolute; left: 26px; top: 454px; width: 696px; height: 30px; background: linear-gradient(90deg, var(--teal-dark), var(--teal)); display: flex; align-items: center; justify-content: space-around; padding: 0 10px; z-index: 2; }
  .award { display: flex; align-items: center; gap: 6px; width: 215px; font-size: 7px; line-height: 9px; color: var(--white); }
  .award-badge { flex: none; width: 14px; height: 14px; border-radius: 50%; background: rgba(255,255,255,.85); }

  .help { position: absolute; top: 548px; left: 0; width: 796px; text-align: center; }
  .help .eyebrow { font-size: 9px; }
  .help-title { margin-top: 8px; font-size: 26px; line-height: 32px; font-weight: 400; }
  .help-text { margin: 16px auto 0; width: 400px; font-size: 8px; line-height: 13px; color: var(--muted); }

  .service-card { position: absolute; background: var(--white); padding: 26px 18px; }
  .card-import { left: 40px; top: 730px; width: 226px; height: 186px; }
  .card-develop { left: 292px; top: 716px; width: 212px; height: 226px; box-shadow: 0 10px 30px rgba(0,0,0,.12); border-right: 4px solid var(--teal); border-bottom: 4px solid var(--teal); border-bottom-right-radius: 18px; padding-top: 40px; }
  .card-install { left: 544px; top: 730px; width: 226px; height: 186px; }
  .card-title { font-size: 11px; line-height: 15px; font-weight: 600; text-transform: uppercase; }
  .feature-list { list-style: none; margin-top: 14px; }
  .feature-list li { display: flex; gap: 7px; font-size: 7px; line-height: 10px; color: var(--muted); margin-bottom: 10px; }
  .feature-list li::before { content: ""; flex: none; width: 9px; height: 9px; margin-top: 1px; border-radius: 50%; border: 1.5px solid var(--teal); }
  .btn-solid { display: inline-block; margin-top: 4px; padding: 0 16px; height: 20px; line-height: 20px; border-radius: 10px; background: var(--teal); color: var(--white); font-size: 7px; font-weight: 500; letter-spacing: .5px; }
</style>
</head>
<body>
  <header class="site-header">
    <div class="brand"><span class="brand-dot"></span>Veldon</div>
    <nav class="main-nav">
      <span>HOME</span><span>SOLUTION</span><span>PRICING</span><span>RESOURCES</span><span>ABOUT</span>
    </nav>
  </header>

  <div class="hero-ghost">er Security</div>
  <div class="hero-visual" role="img" aria-label="Smiling employee working on a laptop in front of teal curved shapes"></div>

  <section class="hero-copy">
    <p class="eyebrow">Cyber security starts with people</p>
    <h1 class="hero-title">Train Your Staff With Veldon<br>And Improve Cyber<br>Security Awareness</h1>
    <div class="demo-row">
      <span class="btn-outline">REQUEST A DEMO</span>
      <svg width="28" height="28" viewBox="0 0 28 28" aria-hidden="true">
        <circle cx="14" cy="14" r="14" fill="#22c3c6"/>
        <path d="M8 14h11M15 10l4 4-4 4" stroke="#fff" stroke-width="2" fill="none" stroke-linecap="round" stroke-linejoin="round"/>
      </svg>
    </div>
  </section>

  <div class="award-band">
    <div class="award"><span class="award-badge"></span>In 2019 Veldon won an industry award for best phishing simulation</div>
    <div class="award"><span class="award-badge"></span>In 2020 Veldon was named a leader for security education platforms</div>
    <div class="award"><span class="award-badge"></span>Analysts listed Veldon among the top awareness training providers</div>
  </div>

  <section class="help">
    <p class="eyebrow">How can we help</p>
    <h2 class="help-title">Test, Train and Engage<br>Your Employees</h2>
    <p class="help-text">Veldon combines organisations to make us all stronger through phishing simulation and training. We give IT staff the technical tools and security awareness your employees need, all in one learning program.</p>
  </section>

  <article class="service-card card-import">
    <h3 class="card-title">Import our training courses in your LMS</h3>
    <ul class="feature-list">
      <li>Run any of the built-in content templates or build your own learning campaign.</li>
      <li>Veldon offers 200 fully customizable modules in 40 languages: videos, quizzes, posters, offline courses and more.</li>
    </ul>
  </article>

  <article class="service-card card-develop">
    <h3 class="card-title">Let us develop a security awareness program</h3>
    <ul class="feature-list">
      <li>Run any of the built-in content templates or build your own learning campaign.</li>
      <li>Veldon offers 200 fully customizable modules in 40 languages: videos, quizzes, posters, offline courses and more.</li>
    </ul>
    <span class="btn-solid">REQUEST DEMO</span>
  </article>

  <article class="service-card card-install">
    <h3 class="card-title">Install the Veldon software on premise or get access to the SaaS version</h3>
    <ul class="feature-list">
      <li>Run any of the built-in content templates or build your own learning campaign.</li>
      <li>Veldon offers 200 fully customizable modules in 40 languages: videos, quizzes, posters, offline courses and more.</li>
    </ul>
  </article>
</body>
</html>
```